International Trade Consulting Firm Seeks Quality Newsletter Design

Our company provides consulting services to Meridian 700 type companies. We compete with the largest consulting companies in the world. However, we have the highest level of expertise in the industry and need to look the most professional and high end. We have very relevant and important information to provide our customers about their compliance and projects. We will have the winning design coded to be an e-newsletter, so it needs to be one page. We want to keep our company colors and logo design in the newsletter, they are attached. We DO NOT want it to look like a mini-version of our website. We want a fresh look to this marketing piece. Newsletter will need to include title, possible sub-heading, space for a feature story, 2 other stories included, and space on either the left or right for short cuts, links or highlights of other articles. Contents/'In this issue' section, about us or branding area, section for relevant links, etc...
Target Market(s)
Meridian 700 companies, High-level management
Industry/Entity Type
Marketing

```html
<!DOCTYPE html>
<html lang="en">
<head>
<meta charset="utf-8">
<title>Harborline News — Vol. 1</title>
<link href="https://fonts.googleapis.com/css2?family=Arimo:wght@400;700&family=Open+Sans:wght@400;600;700&display=swap" rel="stylesheet">
<style>
  :root {
    --black: #050505;
    --deep-green: #1b3619;
    --panel-green: #16301a;
    --band-green: #4c8c3c;
    --band-green-light: #5da048;
    --tan: #d8c27f;
    --cream: #e6dcc0;
    --white: #ffffff;
    --button: #1e8a2b;
    --divider: #8c8466;
  }
  * { box-sizing: border-box; margin: 0; padding: 0; }
  html, body { width: 785px; height: 1200px; overflow: hidden; background: var(--black); }
  .newsletter {
    position: relative; width: 785px; height: 1200px; overflow: hidden;
    font-family: "Open Sans", Arial, sans-serif; color: var(--cream);
    background: var(--black);
  }
  .abs { position: absolute; }

  /* Header */
  .masthead { left: 0; top: 0; width: 785px; height: 138px; background: linear-gradient(#000, #0c0c0c); }
  .browser-note { right: 38px; top: 9px; font-size: 10px; color: var(--cream); }
  .browser-note a { color: var(--cream); text-decoration: underline; }
  .brand-box {
    left: 32px; top: 26px; width: 218px; height: 94px; background: #111;
    display: flex; align-items: center; justify-content: center; gap: 8px;
  }
  .brand-mark { width: 14px; height: 14px; background: var(--band-green-light); }
  .brand-name { font-family: "Open Sans", sans-serif; font-weight: 700; font-size: 22px; color: var(--band-green-light); letter-spacing: 1px; }
  .masthead-title { right: 48px; top: 56px; font-family: "Arimo", Arial, sans-serif; font-weight: 700; font-size: 38px; color: var(--tan); }

  /* Greeting band */
  .greeting-band {
    left: 0; top: 138px; width: 785px; height: 49px;
    background: linear-gradient(90deg, var(--band-green), var(--band-green-light));
  }
  .greeting { left: 41px; top: 146px; font-family: "Arimo", Arial, sans-serif; font-weight: 700; font-size: 27px; color: var(--tan); }
  .volume { right: 38px; top: 157px; font-family: "Arimo", Arial, sans-serif; font-weight: 700; font-size: 17px; color: var(--white); }

  /* Lead area */
  .lead-area { left: 0; top: 187px; width: 785px; height: 284px; background: linear-gradient(90deg, var(--deep-green), #244a22 70%, var(--deep-green)); }
  .photo { background: linear-gradient(135deg, #c9d4dc, #6f7780 55%, #2a2c30); }
  .lead-photo { left: 38px; top: 204px; width: 384px; height: 255px; }
  .article-title { font-family: "Arimo", Arial, sans-serif; font-weight: 700; font-size: 22px; color: var(--tan); text-align: right; width: 290px; }
  .article-body { font-size: 10px; line-height: 14px; text-align: justify; width: 288px; color: var(--cream); }
  .btn {
    display: inline-block; background: var(--button); color: var(--white);
    font-family: "Arimo", Arial, sans-serif; font-weight: 700; font-size: 9.5px;
    padding: 3px 6px; border-radius: 2px;
  }

  /* Section bar */
  .section-bar { left: 0; top: 471px; width: 785px; height: 45px; background: var(--black); }
  .section-label { font-family: "Arimo", Arial, sans-serif; font-weight: 700; color: var(--cream); }
  .section-link { font-family: "Arimo", Arial, sans-serif; font-weight: 700; color: var(--tan); text-decoration: underline; font-size: 19px; }

  /* Columns */
  .col-left { left: 0; top: 516px; width: 413px; height: 644px; background: var(--panel-green); }
  .col-right { left: 418px; top: 516px; width: 367px; height: 644px; background: linear-gradient(#0e1f0f, #152c16); }

  .feature-photo { left: 38px; top: 516px; width: 352px; height: 314px; background: linear-gradient(150deg, #f2ede4, #b7b2ad 55%, #6e6a6a); }
  .feature-title { left: 38px; top: 846px; font-family: "Arimo", Arial, sans-serif; font-weight: 700; font-size: 23px; color: var(--tan); }
  .feature-body { left: 38px; top: 879px; width: 350px; font-size: 9.5px; line-height: 13.5px; text-align: justify; }

  .issue-title { left: 37px; top: 980px; font-family: "Arimo", Arial, sans-serif; font-weight: 700; font-size: 19px; color: var(--cream); }
  .issue-list { left: 38px; top: 1012px; list-style: none; }
  .issue-list li { display: flex; align-items: center; gap: 13px; height: 25px; font-size: 9.5px; }
  .issue-list a { color: var(--tan); text-decoration: underline; }
  .issue-list svg { flex: none; }

  .leader-photo { left: 453px; top: 529px; width: 89px; height: 97px; border: 1px solid var(--tan); background: linear-gradient(#9a9ea4, #4c4f55); }
  .leader-bio { left: 557px; top: 530px; width: 190px; font-size: 7.6px; line-height: 11px; text-align: justify; }
  .story-label { font-family: "Arimo", Arial, sans-serif; font-weight: 700; font-size: 14px; color: var(--cream); text-align: right; width: 200px; }
  .story-link { font-family: "Arimo", Arial, sans-serif; font-weight: 700; font-size: 10.5px; line-height: 12px; color: var(--tan); text-decoration: underline; text-align: right; width: 170px; }
  .story-body { font-size: 6.8px; line-height: 9.5px; text-align: justify; width: 155px; }
  .story1-photo { left: 452px; top: 699px; width: 124px; height: 82px; background: linear-gradient(#dbe8f3, #4f7fa8 60%, #1e3550); }
  .story2-photo { left: 453px; top: 828px; width: 119px; height: 83px; background: radial-gradient(circle at 55% 45%, #8a9aa8, #2b3640 70%); }

  .news-list { left: 460px; top: 1000px; width: 288px; list-style: none; }
  .news-list li { font-size: 9.5px; line-height: 12.5px; padding: 5px 0 9px; border-bottom: 1px dotted var(--divider); margin-bottom: 14px; }
  .news-list li:last-child { border-bottom: none; }

  .footer { left: 0; top: 1160px; width: 785px; height: 40px; background: var(--black); }
  .copyright { left: 0; top: 1176px; width: 785px; text-align: center; font-size: 11.5px; color: var(--cream); }
</style>
</head>
<body>
<div class="newsletter">

  <header>
    <div class="abs masthead"></div>
    <p class="abs browser-note">Is this email not displaying correctly? View it in your <a href="#">browser</a></p>
    <div class="abs brand-box"><span class="brand-mark"></span><span class="brand-name">HARBORLINE</span></div>
    <h1 class="abs masthead-title">Harborline News</h1>
  </header>

  <div class="abs greeting-band"></div>
  <h2 class="abs greeting">We have a good news for you!</h2>
  <span class="abs volume">VOL. 1</span>

  <section>
    <div class="abs lead-area"></div>
    <div class="abs photo lead-photo" role="img" aria-label="Business team meeting around a conference table while a presenter stands at a whiteboard"></div>
    <h3 class="abs article-title" style="left:458px; top:208px;">News Article 1</h3>
    <p class="abs article-body" style="left:458px; top:254px;">Lorem ipsum dolor sit amet, consectetuer adipiscing elit, sed diam nonummy nibh euismod tincidunt ut laoreet dolore magna aliquam erat volutpat. Ut wisi enim ad minim veniam, quis nostrud exerci tation ullamcorper suscipit lobortis nisl ut</p>
    <h3 class="abs article-title" style="left:458px; top:333px;">News Article 2</h3>
    <p class="abs article-body" style="left:459px; top:364px;">Lorem ipsum dolor sit amet, consectetuer adipiscing elit, sed diam nonummy nibh euismod tincidunt ut laoreet dolore magna aliquam erat volutpat. Ut wisi enim ad minim veniam, quis nostrud exerci tation ullamcorper suscipit lobortis nisl ut</p>
    <a class="abs btn" href="#" style="left:682px; top:438px;">READ MORE</a>
  </section>

  <div class="abs section-bar"></div>
  <h2 class="abs section-label" style="left:38px; top:484px; font-size:19px;">Featured Story</h2>
  <h2 class="abs section-link" style="right:41px; top:482px;">LEADER SPEAKS</h2>

  <div class="abs col-left"></div>
  <div class="abs col-right"></div>

  <article>
    <div class="abs feature-photo" role="img" aria-label="Illustration of a crane hook lifting a chained box with a red stripe"></div>
    <h3 class="abs feature-title">Save Money on processing fees</h3>
    <p class="abs feature-body">Lorem ipsum dolor sit amet, consectetuer adipiscing elit, sed diam nonummy nibh euismod tincidunt ut laoreet dolore magna aliquam erat volutpat. Ut wisi enim ad minim veniam, quis nostrud exerci tation ullamcorper suscipit lobortis nisl ut aliquip ex ea commodo consequat. Duis autem vel eum iriure dolor in hendrerit in vulputate velit</p>
    <a class="abs btn" href="#" style="left:325px; top:939px;">READ MORE</a>
  </article>

  <nav>
    <h3 class="abs issue-title">In this Issue</h3>
    <ul class="abs issue-list">
      <li><svg width="10" height="10" viewBox="0 0 10 10"><path d="M1 1 L9 5 L1 9 Z" fill="none" stroke="#d8c27f" stroke-width="1"/></svg><a href="#">Save Money on processing fees</a></li>
      <li><svg width="10" height="10" viewBox="0 0 10 10"><path d="M1 1 L9 5 L1 9 Z" fill="none" stroke="#d8c27f" stroke-width="1"/></svg><a href="#">Advantages of running a business In a foreign Trade zone</a></li>
      <li><svg width="10" height="10" viewBox="0 0 10 10"><path d="M1 1 L9 5 L1 9 Z" fill="none" stroke="#d8c27f" stroke-width="1"/></svg><a href="#">Unlock your International Business Possibilities</a></li>
      <li><svg width="10" height="10" viewBox="0 0 10 10"><path d="M1 1 L9 5 L1 9 Z" fill="none" stroke="#d8c27f" stroke-width="1"/></svg><a href="#">Foreign Trade zone Project Engineering</a></li>
      <li><svg width="10" height="10" viewBox="0 0 10 10"><path d="M1 1 L9 5 L1 9 Z" fill="none" stroke="#d8c27f" stroke-width="1"/></svg><a href="#">Activations with U.S Customs &amp; Border Protection</a></li>
    </ul>
  </nav>

  <aside>
    <div class="abs leader-photo" role="img" aria-label="Portrait of the company founder"></div>
    <p class="abs leader-bio">Daniel Marsh is a founder and President of the Harborline Corporation. Mr. Marsh has been involved in the Foreign-Trade Zones Program since 1989 when he began operating and administering Trade Zone No. 41 in Riverton. This Zone's success set the standard nationwide for Intermodal Trade Zone Operations, JIT manufacturing Operations and distribution operations. In 1994, along with Owen</p>
    <a class="abs btn" href="#" style="left:679px; top:632px;">READ MORE</a>

    <h4 class="abs story-label" style="left:548px; top:667px;">Story 1</h4>
    <div class="abs photo story1-photo" role="img" aria-label="Two business people shaking hands in front of a tall window"></div>
    <a class="abs story-link" href="#" style="left:578px; top:697px;">Unlock your International Business Possibilities</a>
    <p class="abs story-body" style="left:593px; top:734px;">Lorem ipsum dolor sit amet, consectetuer adipiscing elit, sed diam nonummy nibh euismod tincidunt ut laoreet dolore magna aliquam erat volutpat. Ut wisi enim ad minim veniam, quis</p>

    <h4 class="abs story-label" style="left:548px; top:802px;">Story 2</h4>
    <div class="abs story2-photo" role="img" aria-label="Person touching a glowing network of connected points"></div>
    <a class="abs story-link" href="#" style="left:578px; top:828px;">Activations with U.S Customs &amp; Border Protection</a>
    <p class="abs story-body" style="left:595px; top:864px;">Lorem ipsum dolor sit amet, consectetuer adipiscing elit, sed diam nonummy nibh euismod tincidunt ut laoreet dolore magna aliquam erat volutpat. Ut wisi enim ad minim veniam, quis</p>
    <a class="abs btn" href="#" style="left:684px; top:932px;">READ MORE</a>

    <h2 class="abs section-link" style="right:42px; top:969px;">IN THE NEWS</h2>
    <ul class="abs news-list">
      <li>Access to Foreign-Trade Zones: Faster and Easier, Thanks to Recent Federal Regulations</li>
      <li>U.S. Foreign-Trade Zones Program Use Grows Among U.S. Based Manufacturing Operations</li>
      <li>Weston Hale LLC Taps into Foreign-Trade Zone Value for Supply Chain, Partners with Harborline Trade Corporation (Harborline Corp)</li>
    </ul>
  </aside>

  <footer>
    <div class="abs footer"></div>
    <p class="abs copyright">Copyright 2014 Harborline Trade Corporation</p>
  </footer>

</div>
</body>
</html>
```